Redesign of page from emergency manual

Please redesign this PDF to look better. Please don't include any stock photos. It must be legible. Making some words bold is probably a good idea.

Here are some things I like :

https://tarrowbooks.com.au/collections/frontpage/products/the-plk-v2-ebook

https://img-cd.vostramediafiles.com/qa-ejkwPLOTYY_SuCKbZNu411Qwgjv8YssPxEdzXN93hDkSRjLXK8WmfgbmrJW4ZZ3yUPK=w1052-h592-rw

```html
<!DOCTYPE html>
<html lang="en">
<head>
<meta charset="utf-8">
<title>Hypertension, Acute</title>
<link rel="stylesheet" href="https://fonts.googleapis.com/css2?family=Fira+Sans:wght@300;400;600;700&family=Open+Sans:wght@400;600;700&display=swap">
<style>
  :root {
    --sky: #29abe2;
    --ocean: #1479c0;
    --row-strong: #92d3ef;
    --row-soft: #d2ecf8;
    --ink: #1e1e1e;
    --paper: #ffffff;
    --frame: #2a6fb0;
    --revision: #5fc3ee;
  }
  * { box-sizing: border-box; margin: 0; padding: 0; }
  html, body { width: 1200px; height: 932px; overflow: hidden; background: var(--paper); }
  body { font-family: "Open Sans", sans-serif; color: var(--ink); }

  .page { position: relative; width: 1200px; height: 932px; background: var(--paper); }

  /* Header */
  .header-band { position: absolute; left: 0; top: 0; width: 623px; height: 84px; background: var(--sky); }
  .header-shape { position: absolute; left: 622px; top: 0; width: 480px; height: 84px; }
  .title {
    position: absolute; left: 79px; top: 17px;
    font-family: "Fira Sans", sans-serif; font-weight: 600; font-size: 42px;
    color: var(--paper); letter-spacing: 0.5px;
  }
  .subtitle {
    position: absolute; left: 646px; top: 17px; width: 400px;
    font-family: "Fira Sans", sans-serif; font-weight: 600; font-size: 18px; line-height: 21px;
    color: var(--paper); letter-spacing: 0.3px;
  }

  /* Side band */
  .side-band { position: absolute; left: 1144px; top: 0; width: 56px; height: 932px; background: var(--ocean); }
  .side-title {
    position: absolute; left: 1172px; top: 256px;
    writing-mode: vertical-rl;
    font-family: "Fira Sans", sans-serif; font-weight: 300; font-size: 38px;
    color: var(--paper); transform: translateX(-50%);
  }
  .side-revision {
    position: absolute; left: 1166px; top: 752px;
    writing-mode: vertical-rl;
    font-family: "Fira Sans", sans-serif; font-weight: 600; font-size: 15px;
    color: var(--revision); transform: translateX(-50%);
  }

  /* Intro */
  .intro {
    position: absolute; left: 70px; top: 115px; width: 520px; height: 178px;
    border-left: 3px solid var(--sky); padding-left: 17px;
    font-size: 16.5px; line-height: 20px;
  }
  .intro ul { list-style: none; margin-top: 20px; padding-left: 31px; }
  .intro li { position: relative; margin-bottom: 20px; }
  .intro li::before {
    content: ""; position: absolute; left: -22px; top: 5px;
    width: 11px; height: 11px; border-radius: 2px; background: var(--sky);
  }
  .intro .note { display: block; margin-top: 3px; }

  /* BP table */
  .bp-table { position: absolute; left: 646px; top: 115px; width: 430px; border-collapse: collapse; }
  .bp-table caption {
    background: var(--sky); color: var(--paper); height: 37px; line-height: 37px;
    font-family: "Fira Sans", sans-serif; font-weight: 600; font-size: 21px; text-align: left; padding-left: 26px;
  }
  .bp-table th, .bp-table td {
    height: 32px; text-align: center; font-size: 15px; border: 2px solid var(--paper);
  }
  .bp-table th { background: var(--row-strong); font-weight: 700; }
  .bp-table tbody tr:nth-child(odd) td { background: var(--row-soft); }
  .bp-table tbody tr:nth-child(even) td { background: var(--row-strong); }

  /* Caution */
  .caution {
    position: absolute; left: 70px; top: 329px; width: 999px; height: 97px;
    border: 1.5px solid var(--frame); padding: 14px 20px 0 53px;
    font-size: 15px; line-height: 22.5px;
  }
  .caution strong { font-weight: 700; letter-spacing: 0.4px; margin-right: 6px; }
  .caution .indent { padding-left: 86px; display: block; }
  .caution .tail { padding-left: 81px; display: block; }

  /* Drug table */
  .drug-table { position: absolute; left: 67px; top: 459px; width: 1006px; border-collapse: collapse; }
  .drug-table th {
    background: var(--sky); color: var(--paper); height: 36px;
    font-family: "Fira Sans", sans-serif; font-weight: 600; font-size: 22px; border: 2px solid var(--paper);
  }
  .drug-table td { border: 2px solid var(--paper); font-size: 17px; }
  .drug-table .action { width: 226px; text-align: center; line-height: 22px; padding: 0 14px; }
  .drug-table .drugs { padding-left: 126px; }
  .drug-table tr.strong td { background: var(--row-strong); }
  .drug-table tr.soft td { background: var(--row-soft); }
  .drug-table .drugs ul { list-style: none; }
  .drug-table .drugs li { position: relative; line-height: 26px; margin-left: -17px; padding-left: 28px; }
  .drug-table .drugs li::before {
    content: ""; position: absolute; left: 0; top: 8px;
    width: 11px; height: 11px; border-radius: 2px; background: var(--sky);
  }

  /* Differential */
  .differential { position: absolute; left: 76px; top: 790px; width: 1050px; font-size: 15px; line-height: 20px; }
  .differential h2 { font-size: 15px; font-weight: 700; letter-spacing: 0.3px; margin-bottom: 14px; }
  .diff-col { position: absolute; top: 34px; list-style: none; }
  .diff-col.first { left: 0; width: 330px; }
  .diff-col.second { left: 376px; }
  .diff-col.third { left: 816px; top: 37px; }
</style>
</head>
<body>
<main class="page">
  <div class="header-band"></div>
  <svg class="header-shape" viewBox="0 0 480 84" aria-hidden="true">
    <path d="M0 0 H474 C440 32 420 70 370 82 C360 84 355 84 340 84 H0 Z" fill="var(--ocean)"/>
  </svg>
  <h1 class="title">Hypertension, Acute</h1>
  <p class="subtitle">Sustained high blood pressure refractory<br>to treating reversible causes</p>

  <div class="side-band"></div>
  <div class="side-title">Hypertension, Acute</div>
  <div class="side-revision">Revision Feb 2020</div>

  <section class="intro">
    <p>In pediatrics, hypertension is almost always treated by addressing likely causes such as light anesthesia or measurement error:</p>
    <ul>
      <li>Ensure correct BP cuff size: cuff bladder width ~ 40% of limb circumference</li>
      <li>Ensure arterial line transducer is at level of heart<span class="note">- Consider placing arterial line if not already present</span></li>
    </ul>
  </section>

  <table class="bp-table">
    <caption>Hypertensive Blood Pressure Range*</caption>
    <thead>
      <tr><th>Age (yr)</th><th>Systolic</th><th>Diastolic</th></tr>
    </thead>
    <tbody>
      <tr><td>newborn</td><td>&gt;97</td><td>&gt;70</td></tr>
      <tr><td>1 - 3</td><td>&gt;105</td><td>&gt;61</td></tr>
      <tr><td>4 - 12</td><td>&gt;113</td><td>&gt;86</td></tr>
    </tbody>
  </table>

  <section class="caution">
    <strong>CAUTION:</strong>Anti-hypertensive drugs are almost never needed for routine pediatric cases. These medications are used
    <span class="indent">almost exclusively for specialized cardiac, neurosurgical, or endocrine (pheochromocytoma) cases.</span>
    <span class="tail">Consult an expert before use. Rule-out increased ICP.</span>
  </section>

  <table class="drug-table">
    <thead>
      <tr><th>Action</th><th>Drug (IV Dosing)</th></tr>
    </thead>
    <tbody>
      <tr class="strong" style="height:74px">
        <td class="action">Direct smooth muscle relaxation</td>
        <td class="drugs"><ul>
          <li>Sodium nitroprusside 0.5-10 MICROgrams/kg/min</li>
          <li>HydrALAZINE 0.1-0.2 mg/kg (adult dose 5-10 mg)</li>
        </ul></td>
      </tr>
      <tr class="soft" style="height:79px">
        <td class="action">β - Adrenergic blockade</td>
        <td class="drugs"><ul>
          <li>Esmolol 100-500 MICROgrams/kg over 5 min, then 25-300 MICROgrams/kg/min</li>
          <li>Labetalol (also a effect) 0.2-1 mg/kg q 10 min; 0.4-3 mg/kg/hour (infusion)</li>
        </ul></td>
      </tr>
      <tr class="strong" style="height:75px">
        <td class="action">Calcium channel blockade</td>
        <td class="drugs"><ul>
          <li>niCARdapine 0.5-5 MICROgrams/kg/min</li>
          <li>Clevidipine 0.5-3.5 MICROgrams/kg/min</li>
        </ul></td>
      </tr>
      <tr class="soft" style="height:44px">
        <td class="action">D1 - dopamine agonist</td>
        <td class="drugs"><ul>
          <li>Fenoldopam 0.2-0.8 MICROgrams/kg/min</li>
        </ul></td>
      </tr>
    </tbody>
  </table>

  <section class="differential">
    <h2>Consider Differential (Partial):</h2>
    <ul class="diff-col first">
      <li>• Light anesthesia (consider vaporizer or infusion pump empty or malfunctioning)</li>
      <li>• Hypercarbia</li>
    </ul>
    <ul class="diff-col second">
      <li>• Hypoxemia</li>
      <li>• Arterial line transducer too low or BP cuff too small</li>
      <li>• Withdrawal (EtOH or opioid)</li>
    </ul>
    <ul class="diff-col third">
      <li>• Thyroid Storm</li>
      <li>• Pheochromocytoma</li>
      <li>• Drug Error</li>
    </ul>
  </section>
</main>
</body>
</html>
```